Label Design for Sacha Inchi Softgel Capsules

We need a eye catching and unique logo design for our Sacha Inchi softgel with black seed oil and olive extract product. The label will need to include the Company logo with the product brand name TORV'S. The nutrients/consumption details of the product are hereby attached for your necessary designing.

```html
<!DOCTYPE html>
<html lang="en">
<head>
<meta charset="utf-8">
<title>TORV'S Sacha Inchi Softgels Label</title>
<link rel="stylesheet" href="https://fonts.googleapis.com/css2?family=Cinzel:wght@500&family=Josefin+Sans:wght@400&family=Montserrat:wght@300;600&display=swap">
<style>
  :root {
    --page: #ffffff;
    --label-light: #f4f5f6;
    --label-mid: #dfe2e4;
    --brown: #4a2e1f;
    --green: #1f8a4c;
    --ink: #1c1c1c;
    --rule: #3a3a3a;
  }
  html, body {
    margin: 0;
    width: 1195px;
    height: 1200px;
    overflow: hidden;
    background: var(--page);
  }
  .canvas {
    position: relative;
    width: 1195px;
    height: 1200px;
  }
  .label {
    position: absolute;
    left: 317px;
    top: 200px;
    width: 560px;
    height: 800px;
    border-radius: 28px;
    background: linear-gradient(90deg, var(--label-mid) 0%, var(--label-light) 35%, var(--label-light) 65%, var(--label-mid) 100%);
    box-sizing: border-box;
    padding: 110px 0 0 120px;
  }
  .brand-mark {
    display: block;
    width: 58px;
    height: 58px;
    background: var(--brown);
    margin-bottom: 22px;
  }
  .line-name {
    font-family: "Cinzel", serif;
    font-weight: 500;
    font-size: 30px;
    color: var(--green);
    margin: 0 0 26px;
    letter-spacing: 0.5px;
  }
  .brand-name {
    font-family: "Josefin Sans", sans-serif;
    font-weight: 400;
    font-size: 104px;
    line-height: 1;
    color: var(--brown);
    margin: 0 0 34px;
    letter-spacing: 4px;
  }
  .product {
    font-family: "Montserrat", sans-serif;
    color: var(--ink);
    font-size: 27px;
    line-height: 1.12;
    width: 330px;
    margin: 0;
  }
  .product strong { font-weight: 600; display: block; }
  .product span { font-weight: 300; display: block; }
  .rule {
    width: 330px;
    height: 0;
    border-top: 2px solid var(--rule);
    margin: 16px 0;
  }
  .count {
    display: flex;
    align-items: center;
    gap: 10px;
    margin-top: 24px;
    font-family: "Montserrat", sans-serif;
  }
  .count-number {
    background: var(--brown);
    color: #ffffff;
    font-weight: 600;
    font-size: 24px;
    padding: 4px 8px;
  }
  .count-unit {
    font-size: 13px;
    font-weight: 600;
    color: var(--ink);
    letter-spacing: 0.5px;
  }
</style>
</head>
<body>
<main class="canvas">
  <section class="label">
    <span class="brand-mark" aria-hidden="true"></span>
    <p class="line-name">Sacha Inchi</p>
    <h1 class="brand-name">TORV'S</h1>
    <p class="product"><strong>BLACK SEED OIL</strong><span>PLUS EXTRACT</span></p>
    <div class="rule"></div>
    <p class="product"><strong>SACHA INCHI</strong><strong>SEED OIL</strong><span>EXTRACTS</span></p>
    <div class="rule"></div>
    <div class="count">
      <span class="count-number">30</span>
      <span class="count-unit">SOFTGELS</span>
    </div>
  </section>
</main>
</body>
</html>
```